I’d like to see something with similar colors and design concept to the “Your Wallet Knows the Way” book included in attchment

Create a book cover with front cover, and full front, spine and back cover spread.
Simple and clean design. See design inspiration below.
Size 6X9
Title of the book: Find Your Shelf! Veteran Editors Reveal Quiet Methods

Please leave space for 6 authors names on the front cover. Authors names will be provided at a later time.

Back of book should included the name of the publishing company:
Lantern Grove Publishing

As well as the following synopsis
The landscape of the publishing industry is changing. Gone are the days of coveted gatekeepers controlling content and dictating the messages being distributed. With the rise of technology, social media , self-publishing platforms, and independent bookstores, there are increased opportunities for people to share their ideas, messages, and stories with the world through books. The types of books that we’re publishing are also evolving — mini-books, audio books, journals, multi-author books, cook books, children’s books, comic books, coloring books, interactive books, tarot and oracle card decks are all expanding the podium for people to express ideas and influence the culture. More and more entrepreneurs are posturing themselves as thought leaders by leveraging this growing platform.
But that doesn't mean it’s easy.
Even with the expanding platforms and opportunities, only a fraction of people with publishing ambitions are able to achieve this coveted dream held by so many. It can be a daunting process for budding authors trying to maneuver through the writing, packaging, marketing, and publishing processes alone.

In this book you'll find passionate, purpose-driven, and well-versed experts working in the various areas of publishing, eager to help open your eyes to the promise of publishing and effortlessly guide you through the process.

Colors
0094D4
00A9DD
6FCCEA
C7EBF8
E9F6FB
FFF300
FFF600
FEFA6F
FFFEC7
FFFEE8
FFC000
F8CF3A
FAE287
FDF2CF
FEFAEE
F0912C
F2A743
F7CA91
FBE8D2
FDF5EE
EE7325
F08F49
F5BC92
FAE3D3
FDF4ED
6B429C
8869AF
B7A5CE
E3DAEB
F3F0F8

```html
<!DOCTYPE html>
<html lang="en">
<head>
<meta charset="utf-8">
<title>Find Your Shelf! — Cover Spread</title>
<link rel="stylesheet" href="https://fonts.googleapis.com/css2?family=Arimo:wght@400;700&family=Montserrat:wght@400;500&family=Oswald:wght@200;400&display=swap">
<style>
  :root {
    --stage: #d8d8d4;
    --paper: #ffffff;
    --cover-red: #e4463c;
    --accent-cyan: #22e4e6;
    --accent-yellow: #f7e324;
    --ink: #1e1e1e;
    --white: #ffffff;
  }
  * { margin: 0; padding: 0; box-sizing: border-box; }
  html, body { width: 826px; height: 1200px; overflow: hidden; }
  body { background: var(--stage); position: relative; font-family: "Arimo", Arial, sans-serif; }

  .spread {
    position: absolute; left: 23px; top: 330px;
    width: 780px; height: 541px;
    background: var(--paper);
  }

  /* Back cover */
  .back-cover { position: absolute; left: 25px; top: 0; width: 315px; height: 541px; color: var(--ink); }
  .back-title {
    position: absolute; top: 46px; left: 0; width: 100%;
    font-family: "Oswald", sans-serif; font-weight: 400;
    font-size: 34px; line-height: 30px; text-align: center;
    color: var(--cover-red); transform: scaleX(0.86);
  }
  .back-flow {
    position: absolute; top: 120px; left: 0; width: 100%;
    display: flex; flex-direction: column;
  }
  .back-heading {
    font-weight: 700; font-size: 10.5px; line-height: 13px;
    text-align: center; color: var(--cover-red);
  }
  .synopsis {
    font-size: 8.6px; line-height: 11px; text-align: justify; text-align-last: center;
  }
  .synopsis p + p { margin-top: 10px; }
  .back-callout {
    margin-top: 3px;
    font-weight: 700; font-size: 10.5px; line-height: 13px; text-align: center; color: var(--cover-red);
  }
  .outlined-box {
    margin-top: 8px;
    border: 1px solid var(--cover-red); border-radius: 3px;
    padding: 6px 10px; font-size: 8.6px; line-height: 11px; text-align: justify; text-align-last: center;
  }
  .filled-box {
    margin-top: 11px;
    background: var(--cover-red); color: var(--white); border-radius: 3px;
    padding: 6px 10px; font-size: 8.6px; line-height: 11px; text-align: justify; text-align-last: center;
  }
  .publisher {
    margin-top: 9px; text-align: right;
    font-family: "Montserrat", sans-serif; font-size: 7.5px; color: var(--cover-red);
  }
  .price {
    position: absolute; top: 490px; left: 0;
    font-weight: 700; font-size: 10.5px; color: var(--cover-red);
  }

  /* Spine */
  .spine { position: absolute; left: 364px; top: 0; width: 50px; height: 541px; }

  /* Front cover */
  .front-cover {
    position: absolute; left: 434px; top: 16px;
    width: 333px; height: 508px; background: var(--cover-red);
  }
  .front-cover svg { display: block; }
</style>
</head>
<body>
<main class="spread">

  <section class="back-cover">
    <h2 class="back-title">FIND<br>YOUR SHELF</h2>
    <div class="back-flow">
      <h3 class="back-heading">THE LANDSCAPE OF THE PUBLISHING INDUSTRY<br>IS CHANGING.</h3>
      <div class="synopsis">
        <p>Gone are the days of coveted gatekeepers controlling content and dictating the messages being distributed. With the rise of technology, social media , self-publishing platforms, and independent bookstores, there are increased opportunities for people to share their ideas, messages, and stories with the world through books.</p>
        <p>The types of books that we’re publishing are also evolving — mini-books, audio books, journals, multi-author books, cook books, children’s books, comic books, coloring books, interactive books, tarot and oracle card decks are all expanding the podium for people to express ideas and influence the culture. More and more entrepreneurs are posturing themselves as thought leaders by leveraging this growing platform.</p>
      </div>
      <p class="back-callout">BUT THAT DOESN'T MEAN IT’S EASY.</p>
      <p class="outlined-box">Even with the expanding platforms and opportunities, only a fraction of people with publishing ambitions are able to achieve this coveted dream held by so many. It can be a daunting process for budding authors trying to maneuver through the writing, packaging, marketing, and publishing processes alone.</p>
      <p class="filled-box">In this book you'll find passionate, purpose-driven, and well-versed experts working in the various areas of publishing, eager to help open your eyes to the promise of publishing and effortlessly guide you through the process.</p>
      <p class="publisher">LANTERN GROVE PUBLISHING</p>
    </div>
    <p class="price">PRICE:</p>
  </section>

  <section class="spine">
    <svg width="50" height="541" viewBox="0 0 50 541">
      <text class="spine-title" transform="translate(6,53) rotate(90)" font-family="Oswald, sans-serif" font-weight="400" font-size="48" fill="#e4463c" textLength="246" lengthAdjust="spacingAndGlyphs">FIND YOUR SHELF</text>
      <text class="spine-subtitle" transform="translate(31,311) rotate(90)" font-family="Montserrat, sans-serif" font-size="12.5" fill="#1e1e1e" textLength="188" lengthAdjust="spacingAndGlyphs">VETERAN EDITORS REVEAL</text>
      <text class="spine-subtitle" transform="translate(13,311) rotate(90)" font-family="Montserrat, sans-serif" font-size="12.5" fill="#1e1e1e" textLength="111" lengthAdjust="spacingAndGlyphs">QUIET METHODS</text>
    </svg>
  </section>

  <section class="front-cover">
    <svg width="333" height="508" viewBox="0 0 333 508">
      <defs>
        <linearGradient id="silver" x1="0" y1="0" x2="1" y2="1">
          <stop offset="0" stop-color="#f2f2f2"/>
          <stop offset="0.5" stop-color="#d4d4d4"/>
          <stop offset="1" stop-color="#ececec"/>
        </linearGradient>
      </defs>
      <text class="front-title-main" x="166" y="216" text-anchor="middle" font-family="Oswald, sans-serif" font-weight="200" font-size="225" fill="url(#silver)" textLength="262" lengthAdjust="spacingAndGlyphs">FIND</text>
      <text class="front-title-second" x="166" y="295" text-anchor="middle" font-family="Oswald, sans-serif" font-weight="200" font-size="72" fill="url(#silver)" textLength="267" lengthAdjust="spacingAndGlyphs">YOUR SHELF</text>
      <g font-family="Montserrat, sans-serif" text-anchor="middle">
        <text x="166" y="337" font-size="37" font-weight="500" fill="#ffffff" textLength="215" lengthAdjust="spacingAndGlyphs">VETERAN</text>
        <text x="166" y="371" font-size="37" font-weight="500" fill="#ffffff" textLength="190" lengthAdjust="spacingAndGlyphs">EDITORS</text>
        <text x="166" y="398" font-size="25" font-weight="500" fill="#22e4e6" textLength="180" lengthAdjust="spacingAndGlyphs">REVEAL QUIET</text>
        <text x="166" y="421" font-size="25" font-weight="400" fill="#f7e324" textLength="118" lengthAdjust="spacingAndGlyphs">METHODS</text>
        <g class="author-names" font-size="9.6" fill="#ffffff">
          <text x="71" y="446" textLength="84" lengthAdjust="spacingAndGlyphs">AUTHOR NAME 1</text>
          <text x="166" y="446" textLength="86" lengthAdjust="spacingAndGlyphs">AUTHOR NAME 2</text>
          <text x="262" y="446" textLength="86" lengthAdjust="spacingAndGlyphs">AUTHOR NAME 3</text>
          <text x="112" y="466" textLength="84" lengthAdjust="spacingAndGlyphs">AUTHOR NAME 1</text>
          <text x="207" y="466" textLength="86" lengthAdjust="spacingAndGlyphs">AUTHOR NAME 2</text>
          <text x="169" y="485" textLength="86" lengthAdjust="spacingAndGlyphs">AUTHOR NAME 3</text>
        </g>
      </g>
    </svg>
  </section>

</main>
</body>
</html>
```